Smile club flyer design

I am launching an office smile club and would like a design that sits my branding and that is appealing to customers. I have a design (I need a new one) that has all the information.
My website is maplecrestdentalcarewv.com
Brand color is green. The design can be any color

Target Market(s)

Ages 30+

Industry/Entity Type

Dental

Font styles to use
Serif

Requirements
Must have
• Appealing to patients

```html
<!DOCTYPE html>
<html lang="en">
<head>
<meta charset="utf-8">
<title>Maplecrest Dental Care – Smile Club Membership</title>
<link rel="stylesheet" href="https://fonts.googleapis.com/css2?family=Montserrat:wght@600;700;800;900&family=Didact+Gothic&display=swap">
<style>
  :root {
    --teal: #2daea2;
    --teal-soft: #4f877f;
    --ink: #2e3c3d;
    --ink-text: #26302f;
    --pale: #cfe8e7;
    --mint: #c7e3c6;
    --white: #ffffff;
    --backdrop: #666968;
  }
  * { box-sizing: border-box; margin: 0; padding: 0; }
  html, body { width: 1006px; height: 1200px; overflow: hidden; }
  body { background: var(--backdrop); font-family: "Didact Gothic", sans-serif; color: var(--ink-text); }

  .flyer {
    position: absolute; left: 53px; top: 18px; width: 900px; height: 1164px; overflow: hidden;
    background: radial-gradient(ellipse at 45% 40%, #ffffff 0%, #f3fafa 45%, var(--pale) 100%);
    box-shadow: 0 18px 30px rgba(0,0,0,.35);
  }
  .corner-art { position: absolute; left: 0; top: 0; }
  .photo { position: absolute; left: 500px; top: 67px; width: 350px; height: 365px; }

  .brand { position: absolute; left: 44px; top: 70px; color: var(--teal); font-family: "Montserrat", sans-serif; font-weight: 700; text-align: center; width: 270px; }
  .brand-name { font-size: 40px; letter-spacing: -0.5px; line-height: 1; }
  .brand-sub { font-size: 15px; letter-spacing: 6px; margin-top: 6px; }

  .headline { position: absolute; left: 42px; font-family: "Montserrat", sans-serif; font-weight: 800; line-height: 1; }
  .headline-intro { top: 160px; left: 47px; font-size: 42px; color: var(--ink); letter-spacing: .5px; }
  .headline-smile { top: 206px; left: 38px; font-size: 124px; color: var(--teal); letter-spacing: -3px; font-weight: 900; }
  .headline-club { top: 333px; left: 38px; font-size: 72px; color: var(--ink); font-weight: 900; letter-spacing: -1px; }
  .tag-membership {
    position: absolute; left: 240px; top: 344px; width: 252px; height: 51px; background: var(--teal);
    clip-path: polygon(0 0, 93% 0, 100% 100%, 0 100%);
    color: var(--white); font-family: "Montserrat", sans-serif; font-weight: 800; font-size: 28px;
    display: flex; align-items: center; padding-left: 23px;
  }
  .tagline { position: absolute; left: 39px; top: 424px; font-family: "Montserrat", sans-serif; font-weight: 700; font-size: 16.5px; color: var(--ink); }

  .plan { position: absolute; top: 480px; width: 254px; height: 325px; }
  .plan-core { left: 46px; }
  .plan-bright { left: 321px; }
  .plan-total { left: 596px; }
  .plan-head { height: 92px; border-radius: 22px 22px 0 0; color: var(--white); text-align: center; padding-top: 14px; position: relative; z-index: 1; }
  .plan-core .plan-head { background: var(--teal-soft); }
  .plan-bright .plan-head { background: var(--teal); }
  .plan-total .plan-head { background: var(--ink); }
  .plan-title { font-family: "Montserrat", sans-serif; font-weight: 800; font-size: 27px; line-height: 1.05; }
  .plan-type { font-family: "Montserrat", sans-serif; font-weight: 600; font-size: 12px; margin-top: 5px; letter-spacing: .3px; }
  .plan-price-box {
    position: relative; margin-top: -14px; height: 82px; text-align: center;
    border-radius: 50% 50% 0 0 / 16px 16px 0 0;
    background: linear-gradient(180deg, var(--mint) 0%, #e6f3ee 55%, rgba(255,255,255,0) 100%);
    padding-top: 16px; z-index: 2;
  }
  .plan-core .plan-price-box { background: linear-gradient(180deg, #a8d8d3 0%, #e2f2f1 55%, rgba(255,255,255,0) 100%); }
  .plan-price { font-family: "Montserrat", sans-serif; font-weight: 800; font-size: 40px; color: var(--ink); line-height: 1; }
  .plan-period { font-size: 16px; margin-top: 4px; color: var(--ink-text); letter-spacing: .3px; }
  .plan-list { list-style: none; margin-top: 8px; padding-left: 15px; padding-right: 8px; }
  .plan-list li { display: flex; gap: 8px; font-size: 13.5px; line-height: 1.32; margin-bottom: 17px; }
  .plan-list svg { flex: none; width: 15px; height: 16px; margin-top: 1px; fill: var(--teal); }

  .finance-band { position: absolute; left: 0; top: 1033px; width: 900px; height: 218px; top: 823px;
    background: linear-gradient(90deg, #b7dedd 0%, #eaf6f5 55%, #c3e4e2 100%); }
  .finance { position: absolute; left: 40px; top: 40px; width: 360px; text-align: center; }
  .finance-title { font-size: 17.5px; letter-spacing: .4px; }
  .partners { display: flex; justify-content: center; gap: 26px; margin-top: 20px; font-family: "Didact Gothic", sans-serif; font-size: 26px; color: var(--ink); }
  .partner { display: flex; align-items: center; gap: 8px; }
  .partner-dot { width: 14px; height: 14px; border-radius: 50%; background: var(--teal); }
  .finance-plans { font-size: 17.5px; margin-top: 24px; letter-spacing: .4px; }
  .finance-note { font-size: 14px; margin-top: 18px; }

  .refresh { position: absolute; left: 447px; top: 31px; width: 402px; height: 160px; }
  .refresh-head { height: 52px; border-radius: 22px 22px 0 0; background: var(--ink); font-family: "Montserrat", sans-serif; font-weight: 800; font-size: 21px; color: var(--white); display: flex; align-items: center; justify-content: center; gap: 7px; }
  .refresh-head .accent { color: var(--teal); }
  .refresh-body { margin-top: -8px; height: 116px; border-radius: 50% 50% 0 0 / 12px 12px 0 0;
    background: linear-gradient(180deg, var(--mint) 0%, #eef7f3 60%, rgba(255,255,255,0) 100%); display: flex; padding: 18px 0 0 30px; }
  .refresh-price { text-align: center; width: 128px; }
  .refresh-amount { font-family: "Montserrat", sans-serif; font-weight: 800; font-size: 47px; color: var(--ink); line-height: 1; }
  .refresh-limit { font-size: 12.5px; margin-top: 8px; }
  .refresh-items { margin-left: 30px; font-size: 17px; line-height: 1.3; }

  .contact-phone { position: absolute; left: 0; top: 1073px; width: 306px; height: 58px; background: var(--ink); border-radius: 0 30px 30px 0;
    display: flex; align-items: center; gap: 10px; padding-left: 27px; color: var(--white); font-family: "Montserrat", sans-serif; font-weight: 700; font-size: 27px; }
  .contact-phone svg { width: 22px; height: 22px; fill: var(--teal); }
  .contact-web { position: absolute; left: 325px; top: 1091px; display: flex; gap: 12px; font-size: 16px; color: var(--ink-text); align-items: center; }
  .contact-web span { display: flex; align-items: center; gap: 5px; }
  .contact-web svg { width: 13px; height: 13px; fill: var(--teal); }
</style>
</head>
<body>
<main class="flyer">
  <svg class="corner-art" width="900" height="600" viewBox="0 0 900 600" aria-hidden="true">
    <path d="M312,0 C360,60 420,140 500,175 L900,390 L900,0 Z" fill="var(--teal)"/>
    <path d="M406,0 C450,60 500,125 560,148 L900,376 L900,0 Z" fill="var(--ink)"/>
  </svg>

  <svg class="photo" viewBox="0 0 350 365" role="img" aria-label="Photo of a smiling patient during a dental check-up, framed in a tooth shape">
    <defs>
      <linearGradient id="photoTone" x1="0" y1="0" x2="1" y2="1">
        <stop offset="0" stop-color="#e3d4c8"/>
        <stop offset=".45" stop-color="#c9a08a"/>
        <stop offset="1" stop-color="#3a2d28"/>
      </linearGradient>
    </defs>
    <path d="M100,0 C140,0 160,22 175,22 C190,22 215,0 260,0 C330,0 352,60 345,120 C338,180 315,215 305,270 C295,330 285,365 255,365 C225,365 215,310 200,270 C190,240 182,235 175,235 C165,235 150,250 140,285 C128,330 115,365 80,365 C45,365 40,300 30,250 C20,200 0,170 2,110 C5,45 45,0 100,0 Z" fill="url(#photoTone)"/>
  </svg>

  <div class="brand">
    <div class="brand-name">Maplecrest</div>
    <div class="brand-sub">DENTAL CARE</div>
  </div>

  <h1>
    <span class="headline headline-intro">INTRODUCING</span>
    <span class="headline headline-smile">SMILE</span>
    <span class="headline headline-club">CLUB</span>
  </h1>
  <div class="tag-membership">MEMBERSHIP</div>
  <p class="tagline">AFFORDABLE DENTAL CARE – NO INSURANCE REQUIRED</p>

  <svg width="0" height="0" style="position:absolute">
    <symbol id="tooth" viewBox="0 0 16 16"><path d="M4,0.5 C6,0.5 7,1.5 8,1.5 C9,1.5 10,0.5 12,0.5 C15,0.5 15.8,3 15.4,5.5 C15,8 14,9.5 13.3,12 C12.8,14 12.3,15.8 11,15.8 C9.6,15.8 9.3,13 8.7,11.5 C8.4,10.8 7.6,10.8 7.3,11.5 C6.7,13 6.4,15.8 5,15.8 C3.7,15.8 3.2,14 2.7,12 C2,9.5 1,8 0.6,5.5 C0.2,3 1,0.5 4,0.5 Z"/></symbol>
  </svg>

  <section class="plan plan-core">
    <div class="plan-head"><div class="plan-title">CORE CARE</div><div class="plan-type">PREVENTIVE</div></div>
    <div class="plan-price-box"><div class="plan-price">$39</div><div class="plan-period">PER MONTH</div></div>
    <ul class="plan-list">
      <li><svg><use href="#tooth"/></svg>Comprehensive Annual Exam</li>
      <li><svg><use href="#tooth"/></svg>2 Professional Cleanings/Yr</li>
      <li><svg><use href="#tooth"/></svg>Routine Bitewing X-rays</li>
      <li><svg><use href="#tooth"/></svg>10% Savings on Treatment</li>
    </ul>
  </section>

  <section class="plan plan-bright">
    <div class="plan-head"><div class="plan-title">BRIGHT</div><div class="plan-type">COSMETIC</div></div>
    <div class="plan-price-box"><div class="plan-price">$59</div><div class="plan-period">PER MONTH</div></div>
    <ul class="plan-list" style="padding-left:22px">
      <li><svg><use href="#tooth"/></svg>Annual In-Office<br>Whitening (Top &amp; Bottom)</li>
      <li><svg><use href="#tooth"/></svg>Custom Whitening Trays</li>
      <li><svg><use href="#tooth"/></svg>15% Savings on Elective<br>Treatment</li>
    </ul>
  </section>

  <section class="plan plan-total">
    <div class="plan-head"><div class="plan-title">TOTAL SMILE</div><div class="plan-type">PERIODONTAL</div></div>
    <div class="plan-price-box"><div class="plan-price">$89</div><div class="plan-period">PER MONTH</div></div>
    <ul class="plan-list" style="padding-left:21px">
      <li><svg><use href="#tooth"/></svg>3-4 Periodic Maintenance<br>Visits per Year</li>
      <li><svg><use href="#tooth"/></svg>1 Comprehensive Exam</li>
      <li><svg><use href="#tooth"/></svg>Diagnostic X-rays</li>
      <li><svg><use href="#tooth"/></svg>15% Savings on Restorative<br>and Elective Care</li>
    </ul>
  </section>

  <section class="finance-band">
    <div class="finance">
      <p class="finance-title">FLEXIBLE FINANCING FOR TREATMENT</p>
      <div class="partners">
        <span class="partner"><span class="partner-dot"></span>CarePath</span>
        <span class="partner">Summit Dental</span>
      </div>
      <p class="finance-plans">PAYMENT PLANS AVAILABLE</p>
      <p class="finance-note">*$49 Lifetime Activation Fee (Non-Refundable)</p>
    </div>

    <div class="refresh">
      <div class="refresh-head"><span class="accent">New SMILE</span> REFRESH PACKAGE</div>
      <div class="refresh-body">
        <div class="refresh-price"><div class="refresh-amount">$499</div><div class="refresh-limit">Limited Time Offer</div></div>
        <div class="refresh-items">Cleaning +<br>Comprehensive Exam +<br>Whitening</div>
      </div>
    </div>
  </section>

  <div class="contact-phone">
    <svg viewBox="0 0 24 24" aria-hidden="true"><path d="M6.6,10.8 C8,13.6 10.4,16 13.2,17.4 L15.4,15.2 C15.7,14.9 16.1,14.8 16.4,15 C17.5,15.4 18.7,15.6 20,15.6 C20.6,15.6 21,16 21,16.6 L21,20 C21,20.6 20.6,21 20,21 C10.6,21 3,13.4 3,4 C3,3.4 3.4,3 4,3 L7.5,3 C8.1,3 8.5,3.4 8.5,4 C8.5,5.3 8.7,6.5 9.1,7.6 C9.2,7.9 9.1,8.3 8.8,8.6 Z"/></svg>
    (304) 555-0182
  </div>
  <div class="contact-web">
    <span><svg viewBox="0 0 16 16" aria-hidden="true"><path d="M1,3 H15 V13 H1 Z M1,3 L8,9 L15,3" /></svg>info@maplecrestdentalcarewv.com</span>
    <span><svg viewBox="0 0 16 16" aria-hidden="true"><path d="M1,1 L15,6 L9,8 L13,14 L11,15 L7,9 L3,13 Z"/></svg>maplecrestdentalcarewv.com</span>
  </div>
</main>
</body>
</html>
```